we need a design for Water Bottle Lable Wrap
The product is called Corvane Water is a restructured water. its a very healthy and rejuvenating water
we were looking at using as a tag ling Restore, Recover, Rejuvenate.

```html
<!DOCTYPE html>
<html lang="en">
<head>
<meta charset="UTF-8">
<title>Corvane Water – Bottle Label</title>
<link rel="stylesheet" href="https://fonts.googleapis.com/css2?family=Kanit:wght@700&family=Sansita:ital,wght@0,800;1,800&display=swap">
<style>
  :root {
    --paper: #ffffff;
    --royal-blue: #1e6cf8;
    --sky-blue: #0ab1f0;
    --mark-blue: #1598f2;
  }
  html, body {
    margin: 0;
    padding: 0;
    width: 1200px;
    height: 1200px;
    overflow: hidden;
    background: var(--paper);
  }
  .label {
    position: relative;
    width: 1200px;
    height: 1200px;
    background: var(--paper);
  }
  .brand-mark {
    position: absolute;
    left: 378px;
    top: 38px;
    width: 424px;
    height: 424px;
  }
  .brand-name {
    position: absolute;
    left: 0;
    right: 0;
    top: 528px;
    margin: 0;
    text-align: center;
    font-family: "Kanit", sans-serif;
    font-weight: 700;
    font-size: 112px;
    line-height: 1;
    letter-spacing: 2px;
    color: var(--royal-blue);
  }
  .tagline {
    position: absolute;
    left: 0;
    right: 0;
    top: 682px;
    margin: 0;
    padding: 0;
    list-style: none;
    text-align: center;
    font-family: "Sansita", sans-serif;
    font-style: italic;
    font-weight: 800;
    font-size: 56px;
    line-height: 64px;
    letter-spacing: 2px;
    color: var(--sky-blue);
  }
  .product-type {
    position: absolute;
    left: 0;
    right: 0;
    top: 1020px;
    margin: 0;
    text-align: center;
    font-family: "Sansita", sans-serif;
    font-weight: 800;
    font-size: 46px;
    line-height: 1;
    letter-spacing: 3px;
    color: var(--royal-blue);
  }
  .volume {
    position: absolute;
    left: 0;
    right: 0;
    top: 1100px;
    margin: 0;
    text-align: center;
    font-family: "Sansita", sans-serif;
    font-weight: 800;
    font-size: 48px;
    line-height: 1;
    letter-spacing: 1px;
    color: var(--royal-blue);
  }
</style>
</head>
<body>
  <main class="label">
    <svg class="brand-mark" viewBox="0 0 424 424" aria-hidden="true">
      <circle cx="212" cy="212" r="212" fill="var(--mark-blue)"/>
    </svg>
    <h1 class="brand-name">CORVANE</h1>
    <ul class="tagline">
      <li>Restore</li>
      <li>Recover</li>
      <li>Rejuvenate</li>
    </ul>
    <p class="product-type">RESTRUCTURED WATER</p>
    <p class="volume">12oz</p>
  </main>
</body>
</html>
```